Cool wedding invitation

I need a creative graphic designer to create and design a hip, funky yet functional wedding invitation.

To give you an idea of what I am looking for I have create a Glimmerboard Board
http://www.glimmerboard-example.com/tanvelo/invitation/

Please provide your best 2 invitations.

Invitation #1 is designed to be printed on plastic. Use both sides
Invitation #2 is designed to be printed on cardboard

Don't be afraid to express your creativity.

Target Market(s)

This is a wedding invitation so the audience is primarily adults aged between 25 to 65.

Industry/Entity Type

Graphic Designer

Requirements
Nice to have
• The attached a colour palette outlines the colours the invitation may use.
• These colours will form the theme of the wedding.

```html
<!DOCTYPE html>
<html lang="en">
<head>
<meta charset="utf-8">
<title>Ticket Wedding Invitation</title>
<link href="https://fonts.googleapis.com/css2?family=Cinzel:wght@400;700&family=Playfair+Display:ital@1&display=swap" rel="stylesheet">
<style>
  :root {
    --paper: #fdfbfa;
    --maroon: #7a1a2e;
    --band: #7d1630;
    --band-light: #951d3a;
    --ink: #1c1c1c;
    --names: #3a3f44;
    --sky: #8fc4e8;
    --box: #e6e4e3;
    --tick: #bde3f7;
    --stripe: #e4e6e8;
    --monogram: #8dd0ef;
    --backdrop: #f1f1f1;
  }
  html, body {
    margin: 0;
    width: 1200px;
    height: 1000px;
    overflow: hidden;
    background: var(--backdrop);
  }
  .canvas { position: relative; width: 1200px; height: 1000px; }

  .ticket {
    position: absolute;
    left: 100px;
    width: 1000px;
    height: 375px;
    font-family: "Cinzel", serif;
  }
  .ticket--wrapped { top: 80px; }
  .ticket--open { top: 545px; }
  .ticket__outline { position: absolute; inset: 0; }
  .ticket > * { position: absolute; }

  .invite-line {
    top: 22px; left: 95px; width: 490px; text-align: center;
    font-size: 15px; color: var(--ink);
  }
  .rule { background: var(--maroon); height: 2px; left: 95px; width: 485px; }
  .rule--a { top: 55px; } .rule--b { top: 63px; }
  .rule--c { top: 133px; } .rule--d { top: 141px; }
  .rule--e { top: 293px; width: 500px; }

  .couple {
    top: 66px; left: 90px; white-space: nowrap;
    font-size: 50px; color: var(--names); letter-spacing: 1px;
    text-shadow: 0 0 1px #000;
  }
  .couple__and { font-size: 22px; margin: 0 6px; text-shadow: none; }

  .date {
    left: 145px; font-size: 54px; color: var(--sky); line-height: 1; white-space: nowrap;
  }
  .date--day { top: 150px; border-bottom: 2px solid var(--sky); padding-bottom: 2px; }
  .date--full { top: 224px; }

  .venue { top: 302px; left: 110px; font-size: 21px; color: var(--maroon); white-space: nowrap; }
  .venue__label { font-style: italic; text-decoration: underline; }
  .present { top: 328px; left: 95px; font-size: 21px; color: var(--ink); white-space: nowrap; }

  .tear-line {
    left: 620px; top: 10px; height: 355px; width: 0;
    border-left: 5px dashed var(--maroon);
  }

  .vertical {
    writing-mode: vertical-rl;
    transform: rotate(180deg);
    white-space: nowrap;
  }
  .reply {
    left: 641px; top: 50px; height: 280px;
    display: flex; flex-direction: row; justify-content: center; align-items: center;
    text-align: center;
  }
  .reply__lead { font-size: 13px; color: var(--ink); }
  .reply__date { font-size: 20px; color: var(--maroon); margin-top: 0; }

  .names-box {
    left: 695px; top: 8px; width: 165px; height: 340px; background: var(--box);
  }
  .names-box__guide {
    position: absolute; left: 85px; top: 15px; height: 310px;
    border-left: 1px dashed #fff;
  }
  .names-box__label {
    position: absolute; left: 10px; bottom: 14px;
    font-size: 20px; color: var(--ink); text-decoration: underline;
  }

  .rsvp-label { left: 876px; font-size: 14px; color: var(--ink); }
  .rsvp-label--no { top: 30px; }
  .rsvp-label--yes { top: 290px; }
  .rsvp-question {
    left: 872px; top: 90px; height: 170px; text-align: center;
    font-size: 14px; color: var(--maroon); text-decoration: underline;
  }
  .tick-box {
    left: 910px; width: 48px; height: 48px;
    background: var(--tick); border: 2px solid var(--names);
  }
  .tick-box--no { top: 10px; }
  .tick-box--yes { top: 275px; }

  .belly-band {
    left: 365px; top: -14px; width: 300px; height: 403px;
    background: linear-gradient(160deg, var(--band-light), var(--band) 55%, #6a1228);
    box-shadow: 0 0 6px rgba(0,0,0,.25);
  }
  .belly-band__stripe {
    position: absolute; left: 15px; right: 0; top: 175px; height: 58px;
    background: var(--stripe);
  }
  .monogram {
    position: absolute; left: 85px; top: 154px; width: 92px; height: 92px;
    border-radius: 50%; background: var(--monogram); border: 4px solid #111;
    display: flex; align-items: center; justify-content: center;
    font-family: "Playfair Display", serif; font-style: italic;
    font-size: 34px; color: #fff;
  }
</style>
</head>
<body>
<main class="canvas">

  <section class="ticket ticket--wrapped" aria-label="Invitation ticket with belly band">
    <svg class="ticket__outline" width="1000" height="375" viewBox="0 0 1000 375" aria-hidden="true">
      <path d="M12,2 H988 L998,12 V110 A80,80 0 0 0 998,270 V363 L988,373 H12 L2,363 V258 A70,70 0 0 0 2,118 V12 Z"
            fill="var(--paper)" stroke="var(--maroon)" stroke-width="3"/>
    </svg>
    <div class="invite-line">Your Invited to the wedding of</div>
    <div class="rule rule--a"></div><div class="rule rule--b"></div>
    <div class="couple">DANIEL<span class="couple__and">and</span>MARION</div>
    <div class="rule rule--c"></div><div class="rule rule--d"></div>
    <div class="date date--day">SATURDAY</div>
    <div class="date date--full">12 JULY, 2014</div>
    <div class="rule rule--e"></div>
    <div class="venue"><span class="venue__label">Venue:</span> Harbour Gallery</div>
    <div class="present">Please Present this ticket on the day</div>
    <div class="reply vertical">
      <span class="reply__lead">Kindly reply by</span>
      <span class="reply__date">MONDAY 12 MAY 2014</span>
    </div>
    <div class="names-box">
      <div class="names-box__guide"></div>
      <div class="names-box__label vertical">NAMES:</div>
    </div>
    <div class="rsvp-label rsvp-label--no vertical">NO</div>
    <div class="rsvp-question vertical">CAN YOU MAKE IT?</div>
    <div class="rsvp-label rsvp-label--yes vertical">Yes</div>
    <div class="tick-box tick-box--no"></div>
    <div class="tick-box tick-box--yes"></div>

    <div class="belly-band" role="img" aria-label="Maroon belly band with tone-on-tone floral pattern">
      <div class="belly-band__stripe"></div>
      <div class="monogram">D&amp;M</div>
    </div>
  </section>

  <section class="ticket ticket--open" aria-label="Invitation ticket">
    <svg class="ticket__outline" width="1000" height="375" viewBox="0 0 1000 375" aria-hidden="true">
      <path d="M12,2 H988 L998,12 V110 A80,80 0 0 0 998,270 V363 L988,373 H12 L2,363 V258 A70,70 0 0 0 2,118 V12 Z"
            fill="var(--paper)" stroke="var(--maroon)" stroke-width="3"/>
    </svg>
    <div class="invite-line">Your Invited to the wedding of</div>
    <div class="rule rule--a"></div><div class="rule rule--b"></div>
    <div class="couple">DANIEL<span class="couple__and">and</span>MARION</div>
    <div class="rule rule--c"></div><div class="rule rule--d"></div>
    <div class="date date--day">SATURDAY</div>
    <div class="date date--full">12 JULY, 2014</div>
    <div class="rule rule--e"></div>
    <div class="venue"><span class="venue__label">Venue:</span> Harbour Gallery</div>
    <div class="present">Please Present this ticket on the day</div>
    <div class="tear-line"></div>
    <div class="reply vertical">
      <span class="reply__lead">Kindly reply by</span>
      <span class="reply__date">MONDAY 12 MAY 2014</span>
    </div>
    <div class="names-box">
      <div class="names-box__guide"></div>
      <div class="names-box__label vertical">NAMES:</div>
    </div>
    <div class="rsvp-label rsvp-label--no vertical">NO</div>
    <div class="rsvp-question vertical">CAN YOU MAKE IT?</div>
    <div class="rsvp-label rsvp-label--yes vertical">Yes</div>
    <div class="tick-box tick-box--no"></div>
    <div class="tick-box tick-box--yes"></div>
  </section>

</main>
</body>
</html>
```